Velbrook App Homepage Design making customers feel in control of their spend

Hi,
We need a App Homepage design with a UI similar to the attached mock up on an Quillo 4. The app is intended to put customers in control of their usage and spend on their fixed phone, broadband, mobile, gas and electricity.

Please fee free to propose improvements to the background images, icons, colours, etc.

Any questions please let me know.

Thanks
Tomasz

Target Market(s)

Consumer customers

Industry/Entity Type

Internet

Font styles to use
Sans Serif

Colors
3276b5
0255a3
85acd3
cfdeed
ffffff

Requirements
Must have
• Content in line with the guidelines in the attached mock up

```html
<!DOCTYPE html>
<html lang="en">
<head>
<meta charset="utf-8">
<title>Velbrook – Home</title>
<link href="https://fonts.googleapis.com/css2?family=Open+Sans:ital,wght@0,300;0,400;0,600;0,700;1,400&display=swap" rel="stylesheet">
<style>
  :root {
    --navy-deep: #0a1830;
    --navy: #0f2140;
    --navy-light: #1b3452;
    --tile: #0c1a2c;
    --white: #ffffff;
    --sky: #85acd3;
    --pale: #cfdeed;
    --blue: #3276b5;
    --seg-blue: #4a90d9;
    --seg-cyan: #3cc6e0;
    --seg-purple: #9b6fd0;
    --seg-green: #b7d957;
    --seg-red: #e04a4f;
    --flame: #e8542c;
    --phone-green: #a8d83a;
    --wifi: #b07ee6;
    --handset: #43c5d8;
    --bulb: #6fa8e8;
  }
  * { box-sizing: border-box; margin: 0; padding: 0; }
  html, body { width: 1200px; height: 2390px; overflow: hidden; }
  body {
    font-family: "Open Sans", Arial, sans-serif;
    color: var(--white);
    background: var(--navy-deep);
  }
  .screen { position: relative; width: 1200px; height: 2390px; overflow: hidden;
    background: linear-gradient(180deg, var(--navy) 0%, var(--navy-deep) 60%, #081428 100%); }
  .screen__sheen { position: absolute; inset: 0; width: 1200px; height: 2390px; }

  .status-bar { position: absolute; top: 0; left: 0; width: 1200px; height: 86px;
    display: flex; align-items: center; justify-content: space-between; padding: 0 36px;
    font-size: 34px; font-weight: 400; }
  .status-bar__left, .status-bar__right { display: flex; align-items: center; gap: 14px; width: 340px; }
  .status-bar__right { justify-content: flex-end; }
  .status-bar__time { font-weight: 600; }
  .signal { display: flex; gap: 6px; }
  .signal span { width: 16px; height: 16px; border-radius: 50%; border: 2px solid var(--white); }
  .signal span.on { background: var(--white); }
  .battery { width: 64px; height: 30px; border: 3px solid var(--white); border-radius: 6px; padding: 3px; position: relative; }
  .battery::after { content: ""; position: absolute; right: -9px; top: 8px; width: 5px; height: 9px; background: var(--white); border-radius: 0 2px 2px 0; }
  .battery__level { width: 98%; height: 100%; background: var(--white); border-radius: 2px; }

  .app-header { position: absolute; top: 170px; left: 0; width: 1200px; height: 150px;
    display: flex; align-items: center; justify-content: center; }
  .app-header__menu { position: absolute; left: 56px; top: 46px; }
  .app-header__settings { position: absolute; right: 40px; top: 36px; }
  .brand { display: flex; align-items: center; gap: 30px; }
  .brand__mark { width: 110px; height: 110px; border-radius: 50%; background: var(--white); }
  .brand__name { font-size: 96px; font-weight: 600; letter-spacing: -1px; color: var(--white); line-height: 1; }

  .greeting { position: absolute; top: 455px; left: 62px; display: flex; align-items: center; gap: 34px; }
  .greeting__avatar { width: 286px; height: 286px; border-radius: 50%; border: 8px solid var(--blue);
    background: radial-gradient(circle at 45% 40%, #e9d2bf 0%, #b8c9d8 45%, #6f93b6 100%); }
  .greeting__hello { font-size: 62px; font-weight: 700; line-height: 1.2; }
  .greeting__welcome { font-size: 54px; font-style: italic; font-weight: 400; color: var(--sky); margin-top: 34px; }

  .services { position: absolute; top: 948px; left: 38px; width: 1124px; display: flex; justify-content: space-between; }
  .service { width: 196px; height: 196px; border-radius: 50%; background: var(--tile);
    box-shadow: inset 0 0 0 3px rgba(255,255,255,0.04), 0 6px 16px rgba(0,0,0,0.35);
    display: flex; align-items: center; justify-content: center; }

  .charges { position: absolute; top: 1400px; left: 290px; width: 620px; height: 620px; }
  .charges__label { position: absolute; inset: 0; display: flex; flex-direction: column; align-items: center; justify-content: center; text-align: center; }
  .charges__title { font-size: 46px; font-weight: 300; line-height: 1.4; color: var(--pale); }
  .charges__amount { font-size: 74px; font-weight: 700; margin-top: 6px; }

  .allowance { position: absolute; top: 2118px; left: 34px; width: 1140px; display: flex; align-items: center; justify-content: space-between; }
  .allowance__track { position: relative; width: 604px; height: 14px; border-radius: 7px; background: #25364c; }
  .allowance__fill { width: 286px; height: 100%; border-radius: 7px; background: #4a5a6e; }
  .allowance__knob { position: absolute; right: -8px; top: -8px; width: 30px; height: 30px; border-radius: 50%; background: #8c97a4; }
  .allowance__text { font-size: 40px; font-weight: 400; color: var(--pale); }

  .latest-bill { position: absolute; top: 2228px; left: 0; width: 1200px; text-align: center; font-size: 66px; font-weight: 400; }
  .latest-bill__amount { font-size: 86px; font-weight: 700; margin: 0 18px; }
</style>
</head>
<body>
<main class="screen">
  <svg class="screen__sheen" viewBox="0 0 1200 2390" aria-hidden="true">
    <polygon points="0,0 1200,0 1200,360 0,1375" fill="#1c3554" opacity="0.75"/>
  </svg>

  <header class="status-bar">
    <div class="status-bar__left">
      <div class="signal"><span class="on"></span><span class="on"></span><span class="on"></span><span></span><span></span></div>
      <span>VELBROOK</span>
      <svg width="40" height="30" viewBox="0 0 40 30" aria-hidden="true"><path d="M4 11a23 23 0 0 1 32 0M10 17a14 14 0 0 1 20 0" stroke="#fff" stroke-width="4" fill="none" stroke-linecap="round"/><circle cx="20" cy="24" r="4" fill="#fff"/></svg>
    </div>
    <div class="status-bar__time">9:00 AM</div>
    <div class="status-bar__right">
      <svg width="22" height="36" viewBox="0 0 22 36" aria-hidden="true"><path d="M3 10l15 16-7 7V3l7 7L3 26" stroke="#fff" stroke-width="3" fill="none" stroke-linejoin="round"/></svg>
      <span>99%</span>
      <div class="battery"><div class="battery__level"></div></div>
    </div>
  </header>

  <nav class="app-header">
    <svg class="app-header__menu" width="76" height="64" viewBox="0 0 76 64" aria-label="Menu" role="img">
      <rect x="0" y="2" width="76" height="8" rx="4" fill="#fff"/><rect x="0" y="28" width="56" height="8" rx="4" fill="#fff"/><rect x="0" y="54" width="76" height="8" rx="4" fill="#fff"/>
    </svg>
    <div class="brand"><span class="brand__mark"></span><span class="brand__name">Velbrook</span></div>
    <svg class="app-header__settings" width="84" height="84" viewBox="0 0 24 24" aria-label="Settings" role="img">
      <path fill="#fff" d="M19.4 13a7.5 7.5 0 0 0 0-2l2.1-1.6-2-3.4-2.5 1a7.4 7.4 0 0 0-1.7-1L14.9 3.3h-4l-.4 2.7a7.4 7.4 0 0 0-1.7 1l-2.5-1-2 3.4L6.4 11a7.5 7.5 0 0 0 0 2l-2.1 1.6 2 3.4 2.5-1a7.4 7.4 0 0 0 1.7 1l.4 2.7h4l.4-2.7a7.4 7.4 0 0 0 1.7-1l2.5 1 2-3.4zM12.9 15.5a3.5 3.5 0 1 1 0-7 3.5 3.5 0 0 1 0 7z"/>
    </svg>
  </nav>

  <section class="greeting">
    <div class="greeting__avatar" role="img" aria-label="Profile photo of the customer"></div>
    <div>
      <p class="greeting__hello">Good morning Maren</p>
      <p class="greeting__welcome">Welcome to Velbrook</p>
    </div>
  </section>

  <section class="services" aria-label="Services">
    <div class="service" aria-label="Electricity">
      <svg width="96" height="96" viewBox="0 0 48 48" aria-hidden="true" fill="none" stroke="var(--bulb)" stroke-width="2.4" stroke-linecap="round">
        <path d="M24 12a10 10 0 0 0-6 18c1.5 1.2 2 2.5 2 4h8c0-1.5.5-2.8 2-4a10 10 0 0 0-6-18z"/>
        <path d="M20 38h8M21 42h6M24 3v4M10 8l3 3M38 8l-3 3M5 20h4M43 20h-4"/>
      </svg>
    </div>
    <div class="service" aria-label="Gas">
      <svg width="96" height="96" viewBox="0 0 48 48" aria-hidden="true">
        <path fill="var(--flame)" d="M25 4c2 8 12 12 12 24a13 13 0 0 1-26 0c0-7 4-10 6-14 1 4 2 6 4 7 0-6 2-12 4-17z"/>
        <path fill="#ffb07a" d="M24 26c1 4 6 6 6 11a6 6 0 0 1-12 0c0-3 2-5 3-7 .5 2 1.2 3 2 3 0-2.5.3-5 1-7z"/>
      </svg>
    </div>
    <div class="service" aria-label="Mobile">
      <svg width="96" height="96" viewBox="0 0 48 48" aria-hidden="true">
        <rect x="13" y="4" width="22" height="40" rx="4" fill="var(--phone-green)"/>
        <rect x="16" y="9" width="16" height="28" fill="#1d2a12"/>
        <circle cx="24" cy="40.5" r="1.6" fill="#1d2a12"/>
      </svg>
    </div>
    <div class="service" aria-label="Broadband">
      <svg width="96" height="96" viewBox="0 0 48 48" aria-hidden="true" fill="none" stroke="var(--wifi)" stroke-width="3.4" stroke-linecap="round">
        <path d="M4 18a28 28 0 0 1 40 0M10 25a19 19 0 0 1 28 0M16 32a10 10 0 0 1 16 0"/>
        <circle cx="24" cy="38" r="2.6" fill="var(--wifi)" stroke="none"/>
      </svg>
    </div>
    <div class="service" aria-label="Home phone">
      <svg width="96" height="96" viewBox="0 0 48 48" aria-hidden="true">
        <path fill="var(--handset)" d="M14 6l6 7-4 5c2 5 6 9 11 12l5-4 7 6-4 6C23 40 8 25 8 10z"/>
      </svg>
    </div>
  </section>

  <section class="charges" aria-label="Current charges">
    <svg width="620" height="620" viewBox="0 0 620 620" aria-hidden="true">
      <circle cx="310" cy="310" r="300" fill="#0b1a30" stroke="#1f3a58" stroke-width="14"/>
      <circle cx="310" cy="310" r="286" fill="none" stroke="#163050" stroke-width="10"/>
      <g transform="rotate(-90 310 310)" fill="none" stroke-width="54">
        <circle cx="310" cy="310" r="237" stroke="var(--seg-cyan)" stroke-dasharray="289 1200" stroke-dashoffset="0"/>
        <circle cx="310" cy="310" r="237" stroke="var(--seg-purple)" stroke-dasharray="62 1500" stroke-dashoffset="-289"/>
        <circle cx="310" cy="310" r="237" stroke="var(--seg-green)" stroke-dasharray="207 1500" stroke-dashoffset="-351"/>
        <circle cx="310" cy="310" r="237" stroke="var(--seg-red)" stroke-dasharray="476 1500" stroke-dashoffset="-558"/>
        <circle cx="310" cy="310" r="237" stroke="var(--seg-blue)" stroke-dasharray="455 1500" stroke-dashoffset="-1034"/>
      </g>
      <circle cx="310" cy="310" r="210" fill="#0c1b32"/>
    </svg>
    <div class="charges__label">
      <span class="charges__title">Your Current<br>Charges</span>
      <span class="charges__amount">£68.39</span>
    </div>
  </section>

  <section class="allowance">
    <div class="allowance__track"><div class="allowance__fill"></div><span class="allowance__knob"></span></div>
    <p class="allowance__text">Allowance renews in 18 days</p>
  </section>

  <p class="latest-bill">Latest bill :<span class="latest-bill__amount">£75.76</span>on 9 Dec 2016</p>
</main>
</body>
</html>
```